Super Design, sehr nette Konversation, Anpassungen wurden schnell verwirklicht. Bin rund um zufrieden! Gerne wieder.
Zielgruppe
Plattform für KFZ-Dienstleistungen (KFZ-Inspektion, Smart Repair, Fahrzeugaufbereitung, Innenreinigung, etc).
Haben aber im Bereich Fahrzeugpflege eigens ausgeführte Dienstleistungen.
Unsere Dienstleistungen werden während der Arbeit unseres Kunden durchgeführt. Annahmestellen (Schließfachsysteme) sind rund um die Arbeitsstätten unserer Kunden. Wir bieten für ausgewählte Orte auch einen Hol- und Bringservice.
Buchungen laufen über unseren Online-Shop unter glanzamort.de/shop
B2C-Kunden, Vorallem Kunden zwischen 25 und 55 Jahren.
Wir brauchen einen Flyer der dem Kunden unsere verschidenen Leistungen nährer bringt.
Logo in Weiß und Blau hinterlegt. Je nach Design verwenden.
Aufgabenstellung
Flyer in A6 Hochformat, gerne auch beidseitig.
Leistungen:
Reifenwechsel 39,95€ (Mit Reifenwäsche)
Smart-Repair ab 9,95€ (Kratzer und Schrammen, Dellen und Beulen)
KFZ-Inspektion ab 349,95€ (Großer Service & Kleiner Service)
Fahrzeugpflege ab 23,95€ (Innen- & Außenreinigung)
Lackaufbereitung & Politur
Website: glanzamort.de

```html
<!DOCTYPE html>
<html lang="de">
<head>
<meta charset="UTF-8">
<title>glanzamort – Fahrzeugreinigung Ingolstadt</title>
<link rel="stylesheet" href="https://fonts.googleapis.com/css2?family=Inter:wght@300;400&display=swap">
<style>
  :root {
    --bg: #000000;
    --text: #ffffff;
    --rule: #cfcfcf;
    --photo-deep: #0a0c0e;
    --photo-body: #1c2024;
    --photo-steel: #3b4046;
    --photo-glint: #8a9096;
    --photo-mitt: #4f4540;
    --photo-mitt-dark: #2b2522;
    --portrait-a: #2c5aa0;
    --portrait-b: #0c1c3a;
  }
  * { margin: 0; padding: 0; box-sizing: border-box; }
  html, body {
    width: 920px; height: 1200px; overflow: hidden;
    background: var(--bg);
  }
  .flyer {
    position: relative;
    width: 920px; height: 1200px;
    background: var(--bg);
    color: var(--text);
    font-family: "Inter", "Helvetica Neue", Arial, sans-serif;
    font-weight: 300;
    overflow: hidden;
  }
  .hero-photo {
    position: absolute;
    left: 0; top: 0; width: 920px; height: 660px;
    background:
      radial-gradient(ellipse 150px 120px at 480px 130px, var(--photo-mitt) 0%, var(--photo-mitt-dark) 60%, transparent 100%),
      linear-gradient(172deg, transparent 34%, rgba(138,144,150,0.55) 39%, rgba(59,64,70,0.6) 44%, transparent 52%),
      radial-gradient(ellipse 330px 110px at 560px 345px, var(--photo-glint) 0%, var(--photo-steel) 40%, var(--photo-body) 75%, transparent 100%),
      radial-gradient(ellipse 240px 70px at 800px 300px, rgba(90,110,120,0.7) 0%, transparent 100%),
      radial-gradient(ellipse 700px 460px at 640px 280px, var(--photo-body) 0%, var(--photo-deep) 65%, var(--bg) 100%);
    -webkit-mask-image:
      linear-gradient(to bottom, #000 70%, transparent 100%),
      linear-gradient(to right, transparent 0%, #000 32%);
    -webkit-mask-composite: source-in;
            mask-image:
      linear-gradient(to bottom, #000 70%, transparent 100%),
      linear-gradient(to right, transparent 0%, #000 32%);
            mask-composite: intersect;
  }
  .brand {
    position: absolute;
    left: 24px; top: 52px;
    display: flex; align-items: center; gap: 16px;
  }
  .brand-mark {
    width: 44px; height: 44px;
    background: var(--text);
  }
  .brand-name {
    font-size: 42px; font-weight: 400;
    color: var(--text);
  }
  .headline {
    position: absolute;
    left: 28px; top: 520px;
    font-size: 59px; line-height: 51px;
    font-weight: 300;
  }
  .portrait {
    position: absolute;
    left: 716px; top: 548px;
    width: 164px; height: 164px;
    border-radius: 50%;
    border: 2px solid #6c7078;
    background: radial-gradient(circle at 50% 40%, var(--portrait-a) 0%, var(--portrait-b) 85%);
  }
  .divider {
    position: absolute;
    left: 32px; top: 708px;
    width: 526px; height: 1px;
    background: var(--rule);
  }
  .services-title {
    position: absolute;
    left: 32px; top: 746px;
    font-size: 35px; font-weight: 300;
  }
  .services {
    position: absolute;
    left: 32px; top: 818px;
    list-style: none;
  }
  .services li {
    display: flex; align-items: baseline;
    height: 51.5px;
    font-size: 29px; white-space: nowrap;
  }
  .tick {
    width: 34px; height: 30px;
    margin-right: 12px;
    align-self: center;
    flex: none;
  }
  .services .note {
    font-size: 23px; margin-left: 8px;
  }
  .website {
    position: absolute;
    left: 0; right: 0; top: 1136px;
    text-align: center;
    font-size: 37px; font-weight: 300;
  }
</style>
</head>
<body>
<main class="flyer">
  <div class="hero-photo" role="img" aria-label="Nahaufnahme eines nassen, eingeschäumten Autoscheinwerfers mit Waschhandschuh"></div>

  <div class="brand">
    <span class="brand-mark"></span>
    <span class="brand-name">glanzamort</span>
  </div>

  <h1 class="headline">Professionelle<br>Fahrzeugreinigung<br>in Ingolstadt</h1>

  <div class="portrait" role="img" aria-label="Mitarbeiter reinigt ein Fahrzeug mit dem Hochdruckreiniger"></div>

  <div class="divider"></div>

  <h2 class="services-title">Unsere Leistungen für Sie</h2>

  <ul class="services">
    <li><svg class="tick" viewBox="0 0 34 30"><path d="M3 17 L12 27 L32 3" fill="none" stroke="#fff" stroke-width="6" stroke-linejoin="round"/></svg>Reifenwechsel 39,95€<span class="note">(Mit Reifenwäsche)</span></li>
    <li><svg class="tick" viewBox="0 0 34 30"><path d="M3 17 L12 27 L32 3" fill="none" stroke="#fff" stroke-width="6" stroke-linejoin="round"/></svg>Smart-Repair ab 9,95€<span class="note">(Kratzer und Schrammen, Dellen und Beulen)</span></li>
    <li><svg class="tick" viewBox="0 0 34 30"><path d="M3 17 L12 27 L32 3" fill="none" stroke="#fff" stroke-width="6" stroke-linejoin="round"/></svg>KFZ-Inspektion ab 349,95€<span class="note">(Großer Service &amp; Kleiner Service)</span></li>
    <li><svg class="tick" viewBox="0 0 34 30"><path d="M3 17 L12 27 L32 3" fill="none" stroke="#fff" stroke-width="6" stroke-linejoin="round"/></svg>Fahrzeugpflege ab 23,95€<span class="note">(Innen- &amp; Außenreinigung)</span></li>
    <li><svg class="tick" viewBox="0 0 34 30"><path d="M3 17 L12 27 L32 3" fill="none" stroke="#fff" stroke-width="6" stroke-linejoin="round"/></svg>Lackaufbereitung &amp; Politur</li>
  </ul>

  <p class="website">glanzamort.de</p>
</main>
</body>
</html>
```